Clockharbour Homepage Banner 1060 W x 100 H

Please see the attached 'word' document (Also copied below)
Feel free to use any images or logos from our website.
www.clockharbour.com.au

Background:
We are an Australian based official watch distributor/online retailer of international watch brands.

We require a new banner ad (1060 W x 100 H) to replace the existing one on our homepage www.clockharbour.com.au & wish to convey the following information:
*(Please feel free to alter wording, include or exclude points below & generally take creative license (with commercial reality in mind). We sell some luxury watches, so it must look professional & maintain a luxury look & feel.)

Clockharbour Direct:
Revolutionising the retail watch market !

- Buy direct from the official distributor & get world competitive
online prices (with full international warranty, & all original
papers, box & invoice)

- Eliminate all risk of fakes & non-existent factory warranty from
'grey' market sellers

- Free worldwide delivery over A$300

- Order online & 'try-on' in the comfort of your own home.
If you're not 100% happy, just post it back for a full refund or
exchange within 30 days

- Prefer to see & try on before purchase? Visit one of our retail
partner stores.

*** Feel free to copy any images from our website
www.clockharbour.com.au
Updates

Target Market(s)

Luxury watches

Industry/Entity Type

Retail

Font styles to use
Sans Serif

Requirements
Must have
• Visual imagery, text
Nice to have
• Feel free to use your creativity...
Should not have
• Cheap looking or tacky images. We sell some luxury watches, so we need to keep a professional & luxury image.

```html
<!DOCTYPE html>
<html lang="en">
<head>
<meta charset="utf-8">
<title>Clockharbour Direct – Homepage Banners</title>
<link href="https://fonts.googleapis.com/css2?family=Oswald:wght@400;500&family=Roboto+Condensed:wght@400&display=swap" rel="stylesheet">
<style>
  :root {
    --page: #ffffff;
    --ink: #1d1d1f;
    --black: #070707;
    --royal: #1a5ee6;
    --cyan: #11c4f5;
    --sky: #2aa9ec;
    --sky-deep: #1c86d6;
    --mist: #f3f4f6;
    --slate: #4a4845;
    --slate-deep: #2f2d2b;
    --ring-dark: #5a5650;
    --steel: #9aa0a6;
    --headline: "Oswald", "Arial Narrow", sans-serif;
    --body: "Roboto Condensed", "Arial Narrow", sans-serif;
  }
  * { box-sizing: border-box; margin: 0; padding: 0; }
  html, body {
    width: 1200px; height: 1200px; overflow: hidden;
    background: var(--page);
  }
  .canvas { position: relative; width: 1200px; height: 1200px; }
  .banner {
    position: absolute; left: 47px; width: 1106px; height: 104px;
    overflow: hidden;
  }
  .banner--classic { top: 444px; }
  .banner--azure { top: 601px; }
  .banner__art { position: absolute; inset: 0; width: 100%; height: 100%; }

  .headline {
    position: absolute; font-family: var(--headline); font-weight: 500;
    font-size: 58px; line-height: 1; letter-spacing: -0.5px;
    transform: scaleX(0.86); transform-origin: left top;
  }
  .tagline {
    position: absolute; font-family: var(--body); font-size: 20px; line-height: 1;
    transform: scaleX(0.9); transform-origin: left top; white-space: nowrap;
  }
  .offer { position: absolute; left: 866px; top: 14px; width: 236px; height: 84px; }
  .offer__free {
    position: absolute; left: -18px; top: 22px; width: 70px;
    font-family: var(--headline); font-size: 32px; line-height: 1;
    transform: rotate(-90deg); text-align: center;
  }
  .offer__line {
    position: absolute; left: 47px; font-family: var(--headline);
    white-space: nowrap; transform-origin: left top; line-height: 1;
  }
  .offer__delivery { top: 2px; font-size: 22px; transform: scaleX(0.82); }
  .offer__threshold { top: 25px; font-size: 41px; transform: scaleX(0.8); }
  .offer__slogan { top: 75px; left: 1px; font-size: 13.5px; transform: scaleX(0.8); }

  .banner--classic .headline { left: 280px; top: 16px; color: var(--royal); }
  .banner--classic .tagline { left: 281px; top: 72px; color: var(--ink); }
  .banner--classic .offer__free,
  .banner--classic .offer__threshold { color: #fff; }
  .banner--classic .offer__delivery,
  .banner--classic .offer__slogan { color: var(--black); }

  .banner--azure .headline { left: 46px; top: 12px; color: #fff; }
  .banner--azure .tagline { left: 46px; top: 72px; color: var(--slate); }
  .banner--azure .offer { left: 862px; }
  .banner--azure .offer__free,
  .banner--azure .offer__threshold { color: #fff; }
  .banner--azure .offer__delivery,
  .banner--azure .offer__slogan { color: var(--cyan); }
</style>
</head>
<body>
<main class="canvas">

  <section class="banner banner--classic" aria-label="Clockharbour Direct banner, dark variant">
    <svg class="banner__art" viewBox="0 0 1106 104" preserveAspectRatio="none" aria-hidden="false">
      <defs>
        <linearGradient id="classic-mist" x1="0" x2="1">
          <stop offset="0" stop-color="#ffffff"/><stop offset="1" stop-color="#e9ebee"/>
        </linearGradient>
        <linearGradient id="classic-sky" x1="0" x2="1">
          <stop offset="0" stop-color="#3fc4f6"/><stop offset="1" stop-color="#1e9ee8"/>
        </linearGradient>
        <radialGradient id="watch-steel" cx="0.5" cy="0.45" r="0.6">
          <stop offset="0" stop-color="#e2d45a"/><stop offset="0.45" stop-color="#b9b7ad"/><stop offset="1" stop-color="#7c7f83"/>
        </radialGradient>
        <radialGradient id="watch-navy" cx="0.5" cy="0.45" r="0.6">
          <stop offset="0" stop-color="#5c6f86"/><stop offset="0.5" stop-color="#8d949b"/><stop offset="1" stop-color="#2a3c5c"/>
        </radialGradient>
        <radialGradient id="watch-dark" cx="0.45" cy="0.5" r="0.6">
          <stop offset="0" stop-color="#d8dadc"/><stop offset="0.5" stop-color="#6d7074"/><stop offset="1" stop-color="#0c0c0c"/>
        </radialGradient>
      </defs>
      <rect width="1106" height="104" fill="url(#classic-mist)"/>
      <polygon points="690,0 900,0 830,60" fill="var(--sky-deep)"/>
      <polygon points="0,0 286,0 136,104 0,104" fill="var(--black)"/>
      <polygon points="286,0 300,0 150,104 136,104" fill="var(--cyan)"/>
      <polygon points="150,104 200,60 255,104" fill="var(--sky)"/>
      <polygon points="845,0 880,0 812,104 777,104" fill="var(--black)"/>
      <polygon points="880,0 1106,0 1106,104 812,104" fill="url(#classic-sky)"/>
      <g role="img" aria-label="Product photo of a black and steel chronograph wristwatch">
        <ellipse cx="112" cy="52" rx="70" ry="46" fill="url(#watch-dark)"/>
      </g>
      <circle cx="597" cy="72" r="64" fill="var(--black)"/>
      <circle cx="597" cy="72" r="56" fill="#fff"/>
      <g role="img" aria-label="Product photo of a steel chronograph with yellow dial">
        <circle cx="597" cy="72" r="36" fill="url(#watch-steel)"/>
      </g>
      <circle cx="750" cy="72" r="64" fill="var(--black)"/>
      <circle cx="750" cy="72" r="56" fill="#fff"/>
      <g role="img" aria-label="Product photo of a diver chronograph with navy strap">
        <circle cx="750" cy="72" r="38" fill="url(#watch-navy)"/>
      </g>
    </svg>
    <h2 class="headline">BUY DIRECT</h2>
    <p class="tagline">Get world competitive online prices</p>
    <div class="offer">
      <span class="offer__free">FREE</span>
      <span class="offer__line offer__delivery">WORLDWIDE DELIVERY</span>
      <span class="offer__line offer__threshold">OVER A$300</span>
      <span class="offer__line offer__slogan">REVOLUTIONISING THE RETAIL WATCH MARKET!</span>
    </div>
  </section>

  <section class="banner banner--azure" aria-label="Clockharbour Direct banner, blue variant">
    <svg class="banner__art" viewBox="0 0 1106 104" preserveAspectRatio="none">
      <defs>
        <linearGradient id="azure-sky" x1="0" x2="1">
          <stop offset="0" stop-color="#2fa6ee"/><stop offset="0.6" stop-color="#44c2f7"/><stop offset="1" stop-color="#2fb4f2"/>
        </linearGradient>
        <linearGradient id="azure-mist" x1="0" x2="1">
          <stop offset="0" stop-color="#ffffff"/><stop offset="1" stop-color="#eceef1"/>
        </linearGradient>
        <linearGradient id="azure-slate" x1="0" x2="1">
          <stop offset="0" stop-color="#5d5a55"/><stop offset="1" stop-color="#2c2a28"/>
        </linearGradient>
        <radialGradient id="azure-diver" cx="0.5" cy="0.45" r="0.6">
          <stop offset="0" stop-color="#3a4f86"/><stop offset="0.6" stop-color="#1f3570"/><stop offset="1" stop-color="#c1352e"/>
        </radialGradient>
        <radialGradient id="azure-steel" cx="0.5" cy="0.45" r="0.6">
          <stop offset="0" stop-color="#e2d45a"/><stop offset="0.45" stop-color="#b9b7ad"/><stop offset="1" stop-color="#7c7f83"/>
        </radialGradient>
        <radialGradient id="azure-navy" cx="0.5" cy="0.45" r="0.6">
          <stop offset="0" stop-color="#5c6f86"/><stop offset="0.5" stop-color="#8d949b"/><stop offset="1" stop-color="#2a3c5c"/>
        </radialGradient>
      </defs>
      <rect width="1106" height="104" fill="url(#azure-mist)"/>
      <polygon points="820,0 880,0 850,30" fill="var(--sky-deep)"/>
      <polygon points="0,0 422,0 285,104 0,104" fill="url(#azure-sky)"/>
      <polygon points="422,0 445,0 308,104 285,104" fill="var(--black)"/>
      <polygon points="308,104 350,72 380,104" fill="var(--sky)"/>
      <polygon points="850,0 878,0 826,104 798,104" fill="var(--cyan)"/>
      <polygon points="878,0 1106,0 1106,104 826,104" fill="url(#azure-slate)"/>
      <circle cx="472" cy="70" r="64" fill="var(--cyan)"/>
      <circle cx="472" cy="70" r="57" fill="var(--ring-dark)"/>
      <circle cx="472" cy="70" r="53" fill="#fff"/>
      <g role="img" aria-label="Product photo of a diver watch with blue and red bezel">
        <circle cx="472" cy="70" r="34" fill="url(#azure-diver)"/>
      </g>
      <circle cx="618" cy="70" r="64" fill="var(--cyan)"/>
      <circle cx="618" cy="70" r="57" fill="var(--ring-dark)"/>
      <circle cx="618" cy="70" r="53" fill="#fff"/>
      <g role="img" aria-label="Product photo of a steel chronograph with yellow dial">
        <circle cx="618" cy="70" r="34" fill="url(#azure-steel)"/>
      </g>
      <circle cx="770" cy="70" r="64" fill="var(--cyan)"/>
      <circle cx="770" cy="70" r="57" fill="var(--ring-dark)"/>
      <circle cx="770" cy="70" r="53" fill="#fff"/>
      <g role="img" aria-label="Product photo of a diver chronograph with navy strap">
        <circle cx="770" cy="70" r="36" fill="url(#azure-navy)"/>
      </g>
    </svg>
    <h2 class="headline">BUY DIRECT</h2>
    <p class="tagline">Get world competitive online prices</p>
    <div class="offer">
      <span class="offer__free">FREE</span>
      <span class="offer__line offer__delivery">WORLDWIDE DELIVERY</span>
      <span class="offer__line offer__threshold">OVER A$300</span>
      <span class="offer__line offer__slogan">REVOLUTIONISING THE RETAIL WATCH MARKET!</span>
    </div>
  </section>

</main>
</body>
</html>
```